Emergency Medical Training and Events Company Business Needs Business Card Design

We are in need of a business card for our dynamic company expanding its customer base and need to be easily contacted and identified for when we visit with government officials, potential EMS / Fire agencies and county coordinators to arrange for training programs for first responders to better prepare them for critical thinking at critical incidents.

Target Market(s)

EMS/Fire and Event Promoters

Industry/Entity Type

Medical

Contact Information for Business Card

Two cards, comparable designs:

Martin K. Halvey, Principal, m.halvey@rvqtlo.com
Owen Tash, Event and Training Specialist, o.tash@rvqtlo.com

Font styles to use
Other font styles liked:
• Cambria

Colors

Designer to choose colors to be used in the design.

Requirements
Must have
• Company Logo, Spots for Name, Title, Phone Number, Email, Website
• A bullet list stating that we offer, QRB CPR and First Aid Instructors, Hold the Line Instructors, Event EMS, CME's, MCI Training and Planning. We prefer to have a black background for the card but if you can make a blue or white card stand out we would review that as well.
Should not have
• Tacky logos or special sayings ... simple, elegant, professional is the look we seek

```html
<!DOCTYPE html>
<html lang="en">
<head>
<meta charset="utf-8">
<title>Rivqen Training – Business Cards</title>
<link href="https://fonts.googleapis.com/css2?family=Caladea:wght@400;700&display=swap" rel="stylesheet">
<style>
  :root{
    --navy:#1b1d4f;
    --navy-deep:#141640;
    --red:#c8201f;
    --white:#ffffff;
    --backdrop:#8a8b95;
  }
  *{box-sizing:border-box;margin:0;padding:0}
  html,body{width:1200px;height:945px;overflow:hidden}
  body{background:var(--backdrop);font-family:"Caladea",serif;position:relative}

  .card{position:absolute;left:240px;width:720px;height:411px;border-radius:26px;overflow:hidden;background:var(--navy);box-shadow:0 10px 24px rgba(0,0,0,.35)}
  .card--back{top:40px}
  .card--front{top:494px}

  /* back card */
  .brand{position:absolute;top:60px;left:0;right:0;display:flex;align-items:center;justify-content:center;gap:22px}
  .brand__dot{width:74px;height:74px;border-radius:50%;background:var(--white)}
  .brand__name{color:var(--white);font-size:46px;font-weight:700;letter-spacing:1px}
  .offer-heading{position:absolute;top:180px;left:0;right:0;text-align:center;color:var(--red);font-size:24px;font-weight:700;letter-spacing:1px}
  .offer-band{position:absolute;left:0;right:0;display:flex;flex-direction:column;justify-content:center;align-items:center;color:var(--white)}
  .offer-band--certs{top:214px;height:92px;font-size:24px;line-height:1.45}
  .offer-band--services{top:318px;height:76px;background:var(--navy-deep);font-size:21px;line-height:1.4}
  .offer-band__mark{position:absolute;top:8px;width:0;height:0;border-top:9px solid transparent;border-bottom:9px solid transparent}
  .offer-band__mark--left{left:0;border-left:12px solid var(--red)}
  .offer-band__mark--right{right:0;border-right:12px solid var(--red)}

  /* front card */
  .front-art{position:absolute;inset:0}
  .front-brand{position:absolute;left:40px;top:95px;width:200px;display:flex;flex-direction:column;align-items:center;gap:16px}
  .front-brand__dot{width:140px;height:140px;border-radius:50%;background:var(--white)}
  .front-brand__name{color:var(--white);font-size:24px;font-weight:700}
  .person{position:absolute;left:330px;right:36px;text-align:center}
  .person--specialist{top:36px;color:var(--navy)}
  .person__name{font-size:28px;font-weight:700}
  .person__title{font-size:22px}
  .person__mail{font-size:21px;font-weight:700}
  .person--principal{top:156px;color:var(--white)}
  .person--principal .person__name{font-size:30px}
  .contacts{position:absolute;left:330px;right:36px;top:268px;list-style:none;color:var(--white);font-size:22px;font-weight:700;line-height:1.45}
  .contacts li{display:flex;align-items:center;justify-content:center;gap:10px}
  .contacts svg{width:20px;height:20px;flex:none}
</style>
</head>
<body>

<section class="card card--back" aria-label="Card back">
  <div class="brand">
    <span class="brand__dot"></span>
    <span class="brand__name">Rivqen Training</span>
  </div>
  <p class="offer-heading">WE HAVE</p>
  <div class="offer-band offer-band--certs">
    <p>QRB CPR and First Aid Instructors</p>
    <p>Hold the Line Instructors</p>
  </div>
  <div class="offer-band offer-band--services">
    <span class="offer-band__mark offer-band__mark--left"></span>
    <span class="offer-band__mark offer-band__mark--right"></span>
    <p>Event EMS, CME's</p>
    <p>MCI Training and Planning</p>
  </div>
</section>

<section class="card card--front" aria-label="Card front">
  <svg class="front-art" viewBox="0 0 720 411" preserveAspectRatio="none" aria-hidden="true">
    <rect width="720" height="411" fill="var(--red)"/>
    <rect x="280" y="150" width="440" height="66" fill="var(--navy)"/>
    <path d="M0 0 H300 Q200 205 270 411 H0 Z" fill="var(--navy)"/>
    <path d="M300 0 Q200 205 270 411" fill="none" stroke="var(--white)" stroke-width="8"/>
    <path d="M314 0 Q214 205 284 411" fill="none" stroke="var(--red)" stroke-width="6"/>
  </svg>

  <div class="front-brand">
    <span class="front-brand__dot"></span>
    <span class="front-brand__name">Rivqen Training</span>
  </div>

  <div class="person person--specialist">
    <p class="person__name">Owen Tash</p>
    <p class="person__title">Event and Training Specialist</p>
    <p class="person__mail">o.tash@rvqtlo.com</p>
  </div>

  <div class="person person--principal">
    <p class="person__name">Martin K. Halvey</p>
    <p class="person__title">Principal</p>
  </div>

  <ul class="contacts">
    <li>
      <svg viewBox="0 0 20 20"><circle cx="10" cy="10" r="9" fill="var(--navy)"/><rect x="7" y="4.5" width="6" height="11" rx="1.2" fill="none" stroke="var(--white)" stroke-width="1.4"/></svg>
      555-014-2290
    </li>
    <li>
      <svg viewBox="0 0 20 20"><circle cx="10" cy="10" r="9" fill="var(--navy)"/><circle cx="10" cy="10" r="5" fill="none" stroke="var(--white)" stroke-width="1.3"/><path d="M5 10H15M10 5Q7 10 10 15M10 5Q13 10 10 15" fill="none" stroke="var(--white)" stroke-width="1"/></svg>
      www.rvqtlo.com
    </li>
    <li>
      <svg viewBox="0 0 20 20"><circle cx="10" cy="10" r="9" fill="var(--navy)"/><rect x="5" y="6.5" width="10" height="7" fill="none" stroke="var(--white)" stroke-width="1.3"/><path d="M5 6.5 10 11 15 6.5" fill="none" stroke="var(--white)" stroke-width="1.2"/></svg>
      m.halvey@rvqtlo.com
    </li>
  </ul>
</section>

</body>
</html>
```